Healthcare Fraud Criminal Defense Attorney Website

We need to design a website that effectively promotes the message that our firm is at the cutting edge of healthcare law. We want to appear to be trusted experts in the field, who are innovators. We do not want to bore our potential clients with too much content, only enough to make it look like we know what we're doing. They'll have to gain a sense of trust in us to help them once they come to the website. At some part there will have to be room for 3 pictures of the 3 lawyers and a description of who they are.
Updates

Also this is a website that we think looks good: http://www.marvelinlegal.example/

Target Market(s)

Nurses, Doctors and owners of healthcare businesses that have been arrested and/or charged with fraud. They also may have simply been notified that they are under investigation.

Industry/Entity Type

Legal

Number of Pages Required

3 page

Font styles to use
Serif

Colors
000000
606060
b2b2b2
f5f5f5

Requirements
Must have
• A homepage with some content relative to the field. It will likely have 3 or 4 paragraphs with distinct content in each.
• Another page in the website that has a good layout for introducing the 3 attorneys involved.
• Possibly a professional looking "frequently asked questions" third page.
Nice to have
• A call-to-action or info-submission area that does not look cheesy or follow you around the page but is still readily available.
• A phone number must be prominently displayed.

```html
<!DOCTYPE html>
<html lang="en">
<head>
<meta charset="utf-8">
<title>Healthcare Law Attorney</title>
<link rel="stylesheet" href="https://fonts.googleapis.com/css2?family=Cinzel:wght@400;700&family=Lato:ital,wght@0,400;0,700;1,700&family=Questrial&display=swap">
<style>
:root{
  --black:#000000;
  --charcoal:#3a3a3a;
  --graphite:#4a4a4a;
  --slate:#5c5c5c;
  --mid:#606060;
  --silver:#b2b2b2;
  --mist:#f5f5f5;
  --white:#ffffff;
  --ink:#2b2b2b;
  --text:#444444;
}
*{box-sizing:border-box;margin:0;padding:0}
html,body{width:1200px;height:2469px;overflow:hidden;background:var(--white)}
body{position:relative;font-family:'Lato',sans-serif;color:var(--text)}
.abs{position:absolute}

/* header */
.brand{left:155px;top:14px;font-family:'Questrial',sans-serif;font-size:32px;color:#9a9a9a;font-weight:400}
.header-phone{left:890px;top:20px;font-size:22px;color:var(--ink);display:flex;align-items:center;gap:12px}
.main-nav{left:0;top:66px;width:1200px;height:46px;background:var(--slate);display:flex;padding-left:158px}
.main-nav a{display:flex;align-items:center;justify-content:center;height:46px;color:var(--white);font-size:15px;font-weight:700;text-decoration:none;border-right:1px solid #4d4d4d}
.main-nav a.active{background:#eeeeee;color:var(--ink)}

/* hero */
.hero-photo{left:0;top:112px;width:1200px;height:490px;background:linear-gradient(90deg,#6f655b 0%,#b9afa4 18%,#8a7f74 34%,#d0c7bc 52%,#7d7268 70%,#c6bdb2 86%,#6a6057 100%)}
.hero-shade{left:0;top:112px;width:1200px;height:490px;background:linear-gradient(180deg,rgba(40,35,30,.35),rgba(255,255,255,.08) 60%,rgba(60,55,50,.3))}
.hero-title{left:0;top:270px;width:1200px;text-align:center;font-style:italic;font-weight:700;font-size:35px;line-height:50px;color:var(--white);text-shadow:0 2px 5px rgba(0,0,0,.6)}

.feature{top:520px;width:279px;height:234px;background:rgba(60,60,60,.93);text-align:center;color:var(--white)}
.feature .ring{position:absolute;left:95px;top:35px;width:88px;height:88px;border-radius:50%;border:3px solid var(--white);display:flex;align-items:center;justify-content:center}
.feature .ring span{width:76px;height:76px;border-radius:50%;background:var(--white);display:flex;align-items:center;justify-content:center}
.feature p{position:absolute;left:20px;right:20px;top:140px;font-size:16px;line-height:21px;height:63px;display:flex;align-items:center;justify-content:center}
.feature .plus{position:absolute;left:126px;bottom:-13px;width:27px;height:27px;border-radius:50%;background:var(--white);color:var(--mid);font-size:22px;line-height:25px;font-weight:700}

/* welcome */
.section-heading{font-family:'Cinzel',serif;font-weight:700;color:var(--black);font-size:29px}
.welcome-heading{left:99px;top:802px}
.rule{height:2px;background:#d8d8d8}
.rule::before{content:"";position:absolute;left:0;top:0;width:140px;height:2px;background:#9a9a9a}
.portrait{left:94px;top:872px;width:224px;height:223px;background:linear-gradient(160deg,#5b3e2f,#2a2321 55%,#5a5250)}
.welcome-text{left:342px;top:868px;width:392px;font-size:14.5px;line-height:25.8px;color:var(--ink)}
.btn{background:var(--charcoal);color:var(--white);font-size:13px;font-weight:700;display:flex;align-items:center;justify-content:center;letter-spacing:.5px}
.divider{left:762px;top:860px;width:2px;height:240px;background:linear-gradient(180deg,transparent,#e0e0e0 30%,#e0e0e0 70%,transparent)}
.inquiry-heading{left:798px;top:802px}
.field{border:1px solid #cfcfcf;border-radius:3px;background:var(--white);font-size:12px;color:#555;padding:7px 10px}

/* help */
.help-band{left:0;top:1141px;width:1200px;height:464px;background:linear-gradient(90deg,#e6e6e6,#f5f5f5 25%,#ececec 45%,#f7f7f7 70%,#e9e9e9)}
.help-heading{left:0;top:1177px;width:1200px;text-align:center;font-weight:400}
.help-line{left:390px;top:1240px;width:466px;height:1px;background:#cccccc}
.help-line-dark{left:552px;top:1239px;width:96px;height:3px;background:#666}
.service-icon{width:110px;height:110px;border-radius:50%;border:5px solid var(--silver);background:var(--white);display:flex;align-items:center;justify-content:center}
.service-icon.active{background:var(--mid);border-color:#9a9a9a}
.service h3{font-family:'Cinzel',serif;font-weight:700;font-size:21px;color:var(--black);letter-spacing:.5px}
.service p{font-size:12.5px;line-height:21px;color:#555;margin-top:2px}
.service.left{text-align:right;width:310px}
.service.right{text-align:left;width:310px}

/* attorneys */
.attorneys-heading{left:0;top:1645px;width:1200px;text-align:center;font-weight:400}
.attorneys-line{left:415px;top:1689px;width:370px;height:2px;background:#d0d0d0}
.card{top:1730px;width:275px;height:319px;border:1px solid #dcdcdc;background:var(--white);padding:8px}
.card .photo{width:257px;height:221px}
.card h4{font-family:'Cinzel',serif;font-weight:700;font-size:17px;color:var(--black);margin-top:20px;letter-spacing:.3px}
.card small{display:block;font-size:13px;color:#666;margin-top:6px}

/* call band & footer */
.call-band{left:0;top:2104px;width:1200px;height:82px;background:var(--slate);color:var(--white);display:flex;align-items:center;justify-content:center;gap:14px;font-size:29px;letter-spacing:1px}
.call-band strong{font-weight:700}
.footer{left:0;top:2186px;width:1200px;height:237px;background:var(--charcoal);color:var(--white)}
.footer h5{position:absolute;font-size:19px;font-weight:700}
.f-icon{position:absolute;width:30px;height:30px;background:var(--white);border-radius:3px;display:flex;align-items:center;justify-content:center}
.footer .note{position:absolute;font-size:13px;line-height:19px}
.footer .field{border-radius:2px;border:none;font-size:12px;padding:9px 10px}
.legal{left:0;top:2423px;width:1200px;height:46px;background:#111;color:#dddddd;font-size:12px;display:flex;align-items:center;justify-content:center}
</style>
</head>
<body>

<header>
  <div class="abs brand">Healthcare Law Attorney</div>
  <div class="abs header-phone">
    <svg width="20" height="20" viewBox="0 0 24 24"><path fill="#333" d="M6.6 10.8a15.1 15.1 0 0 0 6.6 6.6l2.2-2.2c.3-.3.7-.4 1-.2 1.1.4 2.3.6 3.6.6.6 0 1 .4 1 1V20c0 .6-.4 1-1 1A17 17 0 0 1 3 4c0-.6.4-1 1-1h3.5c.6 0 1 .4 1 1 0 1.3.2 2.5.6 3.6.1.3 0 .7-.2 1z"/></svg>
    123-456-7890
  </div>
  <nav class="abs main-nav">
    <a class="active" style="width:132px">Home</a>
    <a style="width:245px">How We Can Help</a>
    <a style="width:196px">Our Attorneys</a>
    <a style="width:141px">FAQ's</a>
    <a style="width:175px">Contact Us</a>
  </nav>
</header>

<section>
  <div class="abs hero-photo" role="img" aria-label="Close view of classical stone courthouse columns"></div>
  <div class="abs hero-shade"></div>
  <h1 class="abs hero-title">The Government Focuses on Healthcare,<br>So Your Attorney Should Too</h1>

  <div class="abs feature" style="left:120px">
    <div class="ring"><span><svg width="40" height="40" viewBox="0 0 40 40"><circle cx="20" cy="12" r="7" fill="none" stroke="#222" stroke-width="2.5"/><path d="M6 37c0-9 6-14 14-14s14 5 14 14z" fill="none" stroke="#222" stroke-width="2.5"/><path d="M16 24l4 6 4-6" fill="none" stroke="#222" stroke-width="2"/></svg></span></div>
    <p>What Is Medicare And Medicaid Fraud?</p>
    <div class="plus">+</div>
  </div>
  <div class="abs feature" style="left:461px">
    <div class="ring"><span><svg width="42" height="42" viewBox="0 0 42 42"><rect x="15" y="3" width="12" height="36" rx="5" transform="rotate(45 21 21)" fill="#222"/><rect x="15" y="3" width="12" height="36" rx="5" transform="rotate(-45 21 21)" fill="#222"/><rect x="17" y="17" width="8" height="8" transform="rotate(45 21 21)" fill="#fff"/></svg></span></div>
    <p>Health Care Fraud Defense</p>
    <div class="plus">+</div>
  </div>
  <div class="abs feature" style="left:800px">
    <div class="ring"><span><svg width="40" height="40" viewBox="0 0 40 40"><rect x="14" y="6" width="12" height="6" rx="2" fill="none" stroke="#222" stroke-width="2.5"/><rect x="4" y="11" width="32" height="24" rx="3" fill="#222"/><path d="M17 17h6v4h4v6h-4v4h-6v-4h-4v-6h4z" fill="#fff"/></svg></span></div>
    <p>What Should You do If You Are Charged With Medicare/Medicaid Fraud?</p>
    <div class="plus">+</div>
  </div>
</section>

<section>
  <h2 class="abs section-heading welcome-heading">Welcome To Healthcare Law Attorney</h2>
  <div class="abs rule" style="left:94px;top:853px;width:230px"></div>
  <div class="abs portrait" role="img" aria-label="Portrait of the senior attorney in a dark suit"></div>
  <p class="abs welcome-text">Lorem ipsum dolor sit amet, consectetuer adipiscing elitmo sed diam nonummy nibh euismod tincidunt uti laoreetn mori dolore magna aliquam erat volutpat. Ut wisi enim ad minim veniam, quis nostrud exerci tationok ullamcorperl suscipitn lobortis nisl ut aliquip ex ea commodo consequat. Duis hofi autem vel eum iriure dolorn in hendrerit inm nonummy .</p>
  <div class="abs btn" style="left:342px;top:1060px;width:117px;height:35px">READ MORE</div>
  <div class="abs divider"></div>

  <h2 class="abs section-heading inquiry-heading">Quick Inquiry</h2>
  <div class="abs rule" style="left:798px;top:853px;width:304px"></div>
  <div class="abs field" style="left:798px;top:874px;width:302px;height:28px">Name</div>
  <div class="abs field" style="left:798px;top:910px;width:302px;height:28px">Email</div>
  <div class="abs field" style="left:798px;top:946px;width:302px;height:27px">Phone</div>
  <div class="abs field" style="left:798px;top:981px;width:302px;height:63px">Message</div>
  <div class="abs btn" style="left:797px;top:1060px;width:80px;height:35px">SUBMIT</div>
</section>

<section>
  <div class="abs help-band" role="img" aria-label="Faded courthouse colonnade backdrop"></div>
  <h2 class="abs section-heading help-heading">How We Can Help</h2>
  <div class="abs help-line"></div>
  <div class="abs help-line-dark"></div>

  <div class="abs service left" style="left:128px;top:1293px"><h3>Business</h3><p>Lorem ipsum dolor sit amet, consectetuer adipiscing elit, sed diam nonummy nibh euismod tincidunt ut laoreetfgf dolore magna aliquam</p></div>
  <div class="abs service left" style="left:128px;top:1446px"><h3>Personal</h3><p>Lorem ipsum dolor sit amet, consectetuer adipiscing elit, sed diam nonummy nibh euismod tincidunt ut laoreetfgf dolore ma</p></div>
  <div class="abs service right" style="left:764px;top:1293px"><h3>Dispute Resolution</h3><p>Lorem ipsum dolor sit amet, consectetuer adipiscing elit, sed diam nonummy nibh euismod tincidunt ut laoreetfgf dolore magna aliquam</p></div>
  <div class="abs service right" style="left:764px;top:1446px"><h3>Public Sector</h3><p>Lorem ipsum dolor sit amet, consectetuer adipiscing elit, sed diam nonummy nibh euismod tincidunt ut laoreetfgf dolore magna aliquam</p></div>

  <div class="abs service-icon active" style="left:465px;top:1291px"><svg width="56" height="40" viewBox="0 0 56 40"><circle cx="28" cy="9" r="7" fill="#fff"/><path d="M16 34c0-9 5-14 12-14s12 5 12 14z" fill="#fff"/><circle cx="12" cy="13" r="5" fill="#fff"/><path d="M2 32c0-7 4-11 10-11 2 0 3 0 4 1-2 3-3 6-3 10z" fill="#fff"/><circle cx="44" cy="13" r="5" fill="#fff"/><path d="M54 32c0-7-4-11-10-11-2 0-3 0-4 1 2 3 3 6 3 10z" fill="#fff"/><rect x="2" y="35" width="52" height="3" fill="#fff"/></svg></div>
  <div class="abs service-icon" style="left:625px;top:1291px"><svg width="60" height="36" viewBox="0 0 60 36"><path d="M2 8l12-4 10 4 8-3 12 2 14 2v16l-8 2-10 6c-2 1-4 1-5 0L12 26 2 22z" fill="#111"/><path d="M22 12l8-3 8 6c1 1 0 3-2 2l-6-3" fill="none" stroke="#fff" stroke-width="1.5"/><path d="M24 27l-4-3M29 29l-5-4M34 30l-5-4" stroke="#fff" stroke-width="1.5"/></svg></div>
  <div class="abs service-icon" style="left:465px;top:1445px"><svg width="40" height="44" viewBox="0 0 40 44"><circle cx="20" cy="11" r="8" fill="#111"/><path d="M4 42c0-12 7-18 16-18s16 6 16 18z" fill="#111"/><path d="M17 24l3 4 3-4-2 12h-2z" fill="#fff"/></svg></div>
  <div class="abs service-icon" style="left:625px;top:1445px"><svg width="44" height="44" viewBox="0 0 44 44"><circle cx="22" cy="12" r="5" fill="#111"/><path d="M16 42V24c0-4 3-6 6-6s6 2 6 6v18z" fill="#111"/><circle cx="9" cy="17" r="4" fill="#111"/><path d="M4 40V27c0-3 2-5 5-5s5 2 5 5v13z" fill="#111"/><circle cx="35" cy="17" r="4" fill="#111"/><path d="M30 40V27c0-3 2-5 5-5s5 2 5 5v13z" fill="#111"/><path d="M22 1v3M15 3l2 2M29 3l-2 2" stroke="#111" stroke-width="2"/></svg></div>
</section>

<section>
  <h2 class="abs section-heading attorneys-heading">Our Attorneys</h2>
  <div class="abs attorneys-line"></div>
  <div class="abs card" style="left:120px">
    <div class="photo" role="img" aria-label="Headshot of an associate attorney" style="background:linear-gradient(150deg,#7a4a33,#3a2c26 55%,#242424)"></div>
    <h4>Lorem Ipsum Sit Dolor</h4><small>Associate</small>
  </div>
  <div class="abs card" style="left:453px">
    <div class="photo" role="img" aria-label="Headshot of an associate attorney" style="background:linear-gradient(150deg,#3a3a3a,#1e1e1e 60%,#2e3038)"></div>
    <h4>Lorem Ipsum Sit Dolor</h4><small>Associate</small>
  </div>
  <div class="abs card" style="left:785px">
    <div class="photo" role="img" aria-label="Headshot of an associate attorney" style="background:linear-gradient(150deg,#9a8a78,#6d6155 55%,#2a2a2e)"></div>
    <h4>Lorem Ipsum Sit Dolor</h4><small>Associate</small>
  </div>
</section>

<div class="abs call-band">
  <svg width="34" height="34" viewBox="0 0 34 34"><circle cx="17" cy="17" r="15" fill="none" stroke="#fff" stroke-width="2"/><path fill="#fff" d="M12 9c1 0 3 3 3 4s-2 1-2 2 3 5 4 5 1-2 2-2 4 2 4 3-2 4-4 4c-5 0-11-7-11-12 0-2 3-4 4-4z"/></svg>
  <span>CALL NOW &nbsp;- <strong>123 - 456 - 7890</strong></span>
</div>

<footer class="abs footer">
  <h5 style="left:158px;top:32px">Contact Details</h5>
  <div class="f-icon" style="left:156px;top:81px"><svg width="14" height="18" viewBox="0 0 14 18"><path d="M7 0a7 7 0 0 0-7 7c0 5 7 11 7 11s7-6 7-11a7 7 0 0 0-7-7z" fill="#222"/><circle cx="7" cy="7" r="2.5" fill="#fff"/></svg></div>
  <div class="note" style="left:199px;top:78px"><strong>Healthcare Law Attoney</strong><br>consequat vel illum dolor accumsan et, delenit sit facilisi &nbsp;60563</div>
  <div class="f-icon" style="left:156px;top:172px"><svg width="16" height="16" viewBox="0 0 24 24"><path fill="#222" d="M6.6 10.8a15.1 15.1 0 0 0 6.6 6.6l2.2-2.2c.3-.3.7-.4 1-.2 1.1.4 2.3.6 3.6.6.6 0 1 .4 1 1V20c0 .6-.4 1-1 1A17 17 0 0 1 3 4c0-.6.4-1 1-1h3.5c.6 0 1 .4 1 1 0 1.3.2 2.5.6 3.6.1.3 0 .7-.2 1z"/></svg></div>
  <div class="note" style="left:199px;top:178px;font-size:16px">123 456 7890</div>
  <div class="f-icon" style="left:332px;top:172px"><svg width="18" height="14" viewBox="0 0 18 14"><rect width="18" height="14" rx="1" fill="#222"/><path d="M1 1l8 7 8-7" fill="none" stroke="#fff" stroke-width="1.5"/></svg></div>
  <div class="note" style="left:375px;top:180px">info@healthlawcounsel.example</div>

  <h5 style="left:654px;top:32px">Quick Inquiry</h5>
  <div class="abs field" style="left:653px;top:79px;width:185px;height:33px">Your Name</div>
  <div class="abs field" style="left:856px;top:79px;width:186px;height:33px">Your Email</div>
  <div class="abs field" style="left:653px;top:125px;width:389px;height:33px">Your Message</div>
  <div class="abs btn" style="left:653px;top:171px;width:116px;height:33px;background:#6a6a6a;font-size:15px">SUBMIT</div>
</footer>

<div class="abs legal">Copyright 2015 Healthcare Law Attoney. All Rights Reserved.</div>

</body>
</html>
```